Custom Home Page for our new Website

We need a custom home page designed for our new website. We are a successful local copier dealer who is rebuilding our website from scratch. We have decided on Wordpress as our CMS platform and have purchased the professional Corvan theme.

The custom homepage we want will be an imitation of the screen on latest model of copiers we carry. (A picture of this is attached.) the goal is to imitate this style while creating a unique, user-friendly, helpful portal to our website.

The winning entry will make the best transition between the menu structure of our current website (www.plomra.net) and the new layout.

Target Market(s)

Our target market is small to medium sized businesses in the Southeast US. The users of our site are generally IT professionals looking for drivers/support, gatekeepers or other support staff placing service calls and supply orders or prospects looking for information about our company and products.

Requirements
Must have
• Clean design, no distracting elements
• Modern aesthetic
• A color palette that can be used as a basis for the Skin for the rest of the site (The site's look will be based on the winning homepage design.)
• Simple navigation
• Easy to read
• Easily viewed on both desktop and tablet sized screens
• Our logo
• Easily update-able
• Maximum of 4 of the large squares

```html
<!DOCTYPE html>
<html lang="en">
<head>
<meta charset="utf-8">
<title>Plomra — Copier Dealer</title>
<link href="https://fonts.googleapis.com/css2?family=Ubuntu:wght@300;400;500&display=swap" rel="stylesheet">
<style>
:root{
  --red:#d8313b;
  --red-dark:#a91e27;
  --ink:#2a2a2a;
  --muted:#8a8a8a;
  --line:#dcdcdc;
  --footer:#141925;
  --footer-deep:#10141d;
  --footer-text:#5d6474;
  --teal:#22a9c4;
  --green:#22b59a;
  --coral:#e44a4a;
  --gold:#f0c534;
}
*{box-sizing:border-box;margin:0;padding:0}
html,body{width:824px;height:1200px;overflow:hidden;background:#fff}
body{font-family:'Ubuntu',sans-serif;color:var(--ink);position:relative}
.abs{position:absolute}
.brand{left:80px;top:22px;display:flex;align-items:center;gap:8px;font-size:30px;font-weight:500;color:#333}
.brand-dot{width:22px;height:22px;border-radius:50%;background:var(--red)}
.nav{left:320px;top:40px;width:424px;height:29px;background:var(--red);border-bottom:3px solid var(--red-dark);border-radius:3px;display:flex;justify-content:space-around;align-items:center;font-size:12.5px;color:#fff}
.hero{left:0;top:83px;width:824px;height:322px;background:linear-gradient(90deg,#d9d6d2,#efedeb 45%,#e6e3df 80%,#d2cfca)}
.hero-title{left:80px;top:206px;font-weight:400;color:#2b2b2b;line-height:32px}
.hero-title .l1{font-size:21px}
.hero-title .big{font-size:30px}
.copier{left:400px;top:160px;width:345px;height:285px;border-radius:6px;background:linear-gradient(180deg,#3e5a8a 0,#4a6595 18%,#e9e8e4 19%,#d8d6d1 100%)}
.feature{top:470px;width:160px;text-align:center}
.feature .ico{width:65px;height:60px;margin:0 auto;display:flex;align-items:center;justify-content:center;box-shadow:3px 3px 0 rgba(0,0,0,.25)}
.feature h3{font-size:13.5px;font-weight:400;margin-top:13px}
.feature p{font-size:7.5px;color:var(--muted);line-height:13px;margin-top:6px}
.sec-head{display:flex;align-items:center;gap:8px;color:var(--red);font-size:15px;font-weight:400}
.sec-head::before,.sec-head::after{content:"";flex:1;height:1px;background:var(--line)}
.sec-head.left::before{display:none}
.card{top:668px;width:158px;height:96px;border:1px solid #e4e4e4}
.card .shot{position:absolute;left:34px;top:12px;width:88px;height:72px;border-radius:4px;background:linear-gradient(180deg,#cfd3d8,#eceef0)}
.pname{top:775px;width:158px;text-align:center;font-size:12px;color:#333}
.arrow{top:709px}
.body-text{font-size:7.5px;color:var(--muted);line-height:15.5px;font-weight:300}
.footer{left:0;top:953px;width:824px;height:200px;background:var(--footer)}
.footer-bar{left:0;top:1153px;width:824px;height:47px;background:var(--footer-deep);font-size:7.5px;color:var(--footer-text)}
.f-brand{left:80px;top:983px;display:flex;align-items:center;gap:7px;font-size:26px;font-weight:500;color:#fff}
.f-brand span.dot{width:18px;height:18px;border-radius:50%;background:#fff}
.f-title{font-size:10.5px;color:#e6e8ec}
.f-text{font-size:7.5px;color:var(--footer-text);line-height:15.5px}
.f-sub{font-size:9.5px;color:#e6e8ec;margin-bottom:4px}
.social{top:1098px;width:24px;height:24px;border-radius:3px;border-bottom:2px solid rgba(0,0,0,.35)}
.thumb{width:38px;height:38px;background:linear-gradient(180deg,#9ea3a8,#e5e6e8)}
</style>
</head>
<body>
<header>
  <div class="abs brand"><span>Plomra</span><span class="brand-dot"></span></div>
  <nav class="abs nav"><span>Home</span><span>What We Are</span><span>What We Offer</span><span>Support</span><span>Contact Us</span></nav>
</header>

<section>
  <div class="abs hero" role="img" aria-label="Blurred bright office interior"></div>
  <h1 class="abs hero-title"><span class="big">Great</span> <span class="l1">with copiers.</span><br><span class="l1">Even better with</span> <span class="big">people</span></h1>
  <div class="abs copier" role="img" aria-label="Large office multifunction copier with finisher"></div>
</section>

<section>
  <div class="abs feature" style="left:69px">
    <div class="ico" style="background:var(--teal)"><svg width="30" height="30" viewBox="0 0 30 30"><circle cx="15" cy="15" r="12" fill="none" stroke="#fff" stroke-width="2.5"/><circle cx="15" cy="15" r="4" fill="#fff"/></svg></div>
    <h3>Our Philosophy</h3>
    <p>Is simple: work hard to earn your<br>customers and work hard to keep them.</p>
  </div>
  <div class="abs feature" style="left:242px">
    <div class="ico" style="background:var(--green)"><svg width="30" height="30" viewBox="0 0 30 30"><circle cx="15" cy="15" r="12" fill="none" stroke="#fff" stroke-width="2.5"/><path d="M15 15 L21 9" stroke="#fff" stroke-width="2.5"/></svg></div>
    <h3>Our Values</h3>
    <p>You can tell a lot about a company by<br>the things they value.</p>
  </div>
  <div class="abs feature" style="left:415px">
    <div class="ico" style="background:var(--coral)"><svg width="30" height="30" viewBox="0 0 30 30"><path d="M4 12 L15 5 L26 12 V25 H4 Z" fill="none" stroke="#fff" stroke-width="2.2"/><path d="M4 12 L15 20 L26 12" fill="none" stroke="#fff" stroke-width="2.2"/></svg></div>
    <h3>Bill Of Rights</h3>
    <p>We believe each of our clients have<br>certain rights which we must uphold…</p>
  </div>
  <div class="abs feature" style="left:588px">
    <div class="ico" style="background:var(--gold)"><svg width="30" height="30" viewBox="0 0 30 30"><path d="M7 3 H19 L24 8 V27 H7 Z" fill="none" stroke="#fff" stroke-width="2.2"/><circle cx="15" cy="17" r="4" fill="none" stroke="#fff" stroke-width="2"/></svg></div>
    <h3>Awards</h3>
    <p>We sell products that have received a<br>lot of recognition what all the fuss is</p>
  </div>
</section>

<section>
  <h2 class="abs sec-head" style="left:80px;top:623px;width:664px">OUR PRODUCTS</h2>
  <svg class="abs arrow" style="left:68px" width="10" height="12" viewBox="0 0 10 12"><path d="M8 1 L2 6 L8 11" fill="none" stroke="var(--red)" stroke-width="3"/></svg>
  <svg class="abs arrow" style="left:746px" width="10" height="12" viewBox="0 0 10 12"><path d="M2 1 L8 6 L2 11" fill="none" stroke="var(--red)" stroke-width="3"/></svg>
  <div class="abs card" style="left:79px"><div class="shot" role="img" aria-label="Compact copier product photo"></div></div>
  <div class="abs card" style="left:249px"><div class="shot" role="img" aria-label="Copier product photo"></div></div>
  <div class="abs card" style="left:418px"><div class="shot" role="img" aria-label="Copier product photo"></div></div>
  <div class="abs card" style="left:587px"><div class="shot" role="img" aria-label="Copier product photo"></div></div>
  <div class="abs pname" style="left:79px">Kestrel KX-208D/S</div>
  <div class="abs pname" style="left:249px">Kestrel KX-M160</div>
  <div class="abs pname" style="left:418px">Kestrel KX-M162</div>
  <div class="abs pname" style="left:587px">Kestrel KX-M205</div>
</section>

<section>
  <h2 class="abs sec-head left" style="left:79px;top:819px;width:410px">WELCOME TO PLOMRA</h2>
  <p class="abs body-text" style="left:79px;top:850px;width:415px">Lorem Ipsum is simply dummy text of the printing and typesetting industry. Lorem Ipsum has been the industry's standard dummy text ever since the 1500s, when an unknown printer took a galley of type and scrambled it to make a type specimen book. It has survived not only five centuries, but also the leap into electronic typesetting, remaining essentially unchanged. It was popularised in the 1960s with the release of Letraset sheets containing Lorem Ipsum passages.</p>
  <h2 class="abs sec-head left" style="left:527px;top:819px;width:217px">ABOUT US</h2>
  <p class="abs body-text" style="left:527px;top:850px;width:217px">Lorem Ipsum is simply dummy text of the printing and typesetting industry. Lorem Ipsum has been the industry's standard dummy text ever since the 1500s, when an unknown printer took a galley of type and scrambled it to make a type specimen book.</p>
</section>

<footer>
  <div class="abs footer"></div>
  <div class="abs f-brand"><span>Plomra</span><span class="dot"></span></div>
  <p class="abs f-text" style="left:80px;top:1035px;width:210px">Lorem Ipsum is simply dummy text of the printing and typesetting industry. Lorem Ipsum has been the industry's standard.</p>
  <div class="abs social" style="left:80px;background:#2fa3d6"></div>
  <div class="abs social" style="left:111px;background:#2f4f8f"></div>
  <div class="abs social" style="left:142px;background:#c91f2c"></div>
  <div class="abs social" style="left:173px;background:#2b8f3e"></div>

  <div class="abs f-title" style="left:325px;top:978px">Recent Posts</div>
  <p class="abs f-text" style="left:325px;top:998px;width:110px;color:#4d5363">Lorem Ipsum is simply dummy text of the printing and typesetting iLorem Ipsum has been the industry's standard dummy since the 1500s, when an unknown printer took a galley of type and scrambled it to make a type specimen</p>

  <div class="abs f-title" style="left:487px;top:978px">Contact Us</div>
  <div class="abs" style="left:487px;top:1000px">
    <div class="f-sub">Brookhaven</div>
    <p class="f-text">118 Alder Creek Road<br>Brookhaven, SC 29000<br>Tel : 555.014.2231</p>
  </div>
  <div class="abs" style="left:487px;top:1077px">
    <div class="f-sub">Marlow</div>
    <p class="f-text">42-B Linden Way<br>Marlow, NC 28000<br>Tel : 555.019.4470</p>
  </div>

  <div class="abs f-title" style="left:620px;top:978px">Image Gallery</div>
  <div class="abs" style="left:619px;top:1006px;display:grid;grid-template-columns:repeat(3,38px);gap:6px" role="img" aria-label="Gallery of copier photos">
    <div class="thumb"></div><div class="thumb"></div><div class="thumb"></div>
    <div class="thumb"></div><div class="thumb"></div><div class="thumb"></div>
  </div>

  <div class="abs footer-bar">
    <div class="abs" style="left:80px;top:20px;word-spacing:2px">Who We Are &nbsp;I&nbsp; What We Offer &nbsp;I&nbsp; Support &nbsp;I&nbsp; Contact Us &nbsp;I&nbsp; Home</div>
    <div class="abs" style="right:80px;top:20px">Copiright © 2013 Plomra, Inc</div>
  </div>
</footer>
</body>
</html>
```